Wedding Startup Full Website Design

We've just completed our online platform and need to create a website that represents our brand and vision, and clearly communicates our features and value proposition to potential users. There are a minimum of 4 pages that need to be designed. One geared toward wedding professionals (venues/vendors/coordinators), another toward engaged couples, one showcasing features, and an 'About Us' page.

The designer will creative freedom to create a unique UI/UX as long as it represents our brand and is relevant to our target audience/market. The ideal candidate will be able to assume the mindset of someone working in the wedding industry and/or an engaged couple. Ability to create illustrations is a plus.

Copy will be provided as needed. We will reimburse for stock images (pending approval before purchasing), but sourcing the stock images will be the responsibility of the designer.

Our current website: https://www.marquiso.com
Updates

Still waiting for a design that stands out from the rest and aligns with the creative brief.

Target Market(s)

Wedding Professionals and Engaged Couples

Industry/Entity Type

Wedding

Number of Pages Required

4 page

Font styles to use
Sans Serif

Colors
ffffff
fbd4d5
f59195
33a6d7
cadf82
86cfc6

Requirements
Must have
• Common sense stuff like having a unified brand that accurately represents our platform, speaks to our target market, and clearly articulates our vision
Nice to have
• Illustrations
Should not have
• Overly cheesy or childish. We want to be professional but still embrace the wedding culture.

```html
<!DOCTYPE html>
<html lang="en">
<head>
<meta charset="utf-8">
<title>Marquiso — About Us</title>
<link href="https://fonts.googleapis.com/css2?family=Bree+Serif&display=swap" rel="stylesheet">
<style>
  :root {
    --teal: #0f9487;
    --teal-line: #2a9d92;
    --ink: #1e1e1e;
    --white: #ffffff;
    --header-bg: rgba(34, 34, 34, 0.88);
    --card-bg: #ebebeb;
    --card-border: #9a9a9a;
    --muted: #7a7a7a;
    --logo-blue: #5aa7dd;
  }
  * { box-sizing: border-box; margin: 0; padding: 0; }
  html, body { width: 1040px; height: 1200px; overflow: hidden; background: var(--white); }
  body { font-family: "Bree Serif", Georgia, serif; color: var(--ink); position: relative; }

  .hero {
    position: absolute; left: 0; top: 0; width: 1040px; height: 392px;
    background: linear-gradient(100deg, #3f5a26 0%, #5f7a35 35%, #8aa45a 60%, #3b4a3a 80%, #6e8a48 100%);
  }
  .site-header {
    position: absolute; left: 0; top: 0; width: 1040px; height: 88px;
    background: var(--header-bg);
  }
  .brand {
    position: absolute; left: 64px; top: 18px;
    font-size: 42px; color: var(--logo-blue); line-height: 1;
  }
  .main-nav { position: absolute; left: 350px; top: 31px; display: flex; gap: 20px; }
  .main-nav a { font-size: 21px; color: var(--white); text-decoration: none; line-height: 1; }
  .main-nav a.is-active { color: var(--teal); }
  .demo-button {
    position: absolute; left: 808px; top: 21px; width: 160px; height: 43px;
    border: 2px solid var(--teal); color: var(--teal);
    font-size: 21px; display: flex; align-items: center; justify-content: center; text-decoration: none;
  }

  .section-title {
    position: absolute; left: 0; width: 1040px; text-align: center;
    font-size: 29px; color: var(--teal); font-weight: 400; line-height: 1;
  }
  .divider { position: absolute; left: 220px; width: 600px; height: 0; border-top: 1.5px solid var(--teal-line); }

  .mission {
    position: absolute; left: 0; top: 489px; width: 516px; height: 407px;
    background: linear-gradient(160deg, #1a1614 0%, #3a2f28 45%, #5a4a3e 75%, #8a7868 100%);
    padding: 32px 30px 0 53px; color: var(--white);
  }
  .mission h2 { font-size: 29px; font-weight: 400; color: var(--teal); line-height: 1; margin-bottom: 14px; }
  .mission p { font-size: 18.6px; line-height: 25.6px; margin-bottom: 25.6px; hyphens: auto; }

  .value { position: absolute; left: 568px; width: 470px; height: 100px; }
  .value svg { position: absolute; left: 0; top: 0; }
  .value h3 { position: absolute; left: 148px; font-size: 19px; font-weight: 400; color: var(--teal); line-height: 1; }
  .value p { position: absolute; left: 148px; width: 300px; font-size: 16px; line-height: 20px; }

  .board { position: absolute; top: 1008px; width: 290px; height: 164px; border: 2px solid var(--card-border); background: var(--card-bg); }
  .board-banner { height: 94px; }
  .board-avatar { position: absolute; left: 14px; top: 62px; width: 64px; height: 64px; border-radius: 50%; border: 3px solid #e0e0e0; background: #b8bcc0; }
  .board-name { position: absolute; right: 16px; top: 102px; font-size: 18px; color: var(--teal); line-height: 1.1; }
  .board-role { position: absolute; right: 16px; top: 128px; font-size: 14px; color: var(--muted); }
</style>
</head>
<body>
  <div class="hero" role="img" aria-label="Bride and groom smiling at each other in a green meadow beside a floral arch"></div>

  <header class="site-header">
    <div class="brand">Marquiso</div>
    <nav class="main-nav">
      <a class="is-active" href="#">ABOUT US</a>
      <a href="#">FEAYURES</a>
      <a href="#">FOR COUPLES</a>
    </nav>
    <a class="demo-button" href="#">ACCESS DEMO</a>
  </header>

  <h1 class="section-title" style="top:402px;">OUR VISION</h1>
  <div class="divider" style="top:455px;" aria-hidden="true"></div>

  <section class="mission" role="img" aria-label="Softly lit wedding reception table behind the mission statement">
    <h2>MISSION STATEMENT</h2>
    <p>Weddings are one the most memorable events in people's life. Unfortunately planning a wedding is filled with stress, often leaving wedding pro&shy;fessionals and their clients with soured memo&shy;ries.</p>
    <p>Our vision at Marquiso is to revamp the way wed&shy;dings are planned on both sides of the process (wedding professionals and their clients). We aim to reduce the stress of everyone involved, and make the engagement season and wedding day memorable for the right reasons.</p>
  </section>

  <div class="value" style="top:497px;">
    <svg width="90" height="80" viewBox="0 0 90 80" aria-hidden="true" fill="none" stroke="var(--teal)" stroke-width="3" stroke-linecap="round">
      <path d="M30 18 a12 12 0 0 1 12 20 v8 h-12 v-8 a12 12 0 0 1 0 -20z"/>
      <line x1="30" y1="50" x2="42" y2="50"/>
      <line x1="36" y1="0" x2="36" y2="6"/><line x1="18" y1="6" x2="22" y2="11"/><line x1="54" y1="6" x2="50" y2="11"/>
      <line x1="8" y1="24" x2="14" y2="24"/><line x1="58" y1="24" x2="64" y2="24"/>
      <path d="M8 72 h36 l38 -14 v-6 h-26 l-14 8 h-26 z" fill="var(--teal)"/>
    </svg>
    <h3 style="top:6px;">INSPIRE</h3>
    <p style="top:32px;">Inspire innovation and bringing dream weddings to life.</p>
  </div>

  <div class="value" style="top:634px;">
    <svg width="90" height="80" viewBox="0 0 90 80" aria-hidden="true" fill="none" stroke="var(--teal)" stroke-width="3" stroke-linecap="round">
      <path d="M8 10 h22 l-4 22 h-14 z"/><line x1="19" y1="32" x2="16" y2="70"/><line x1="6" y1="70" x2="26" y2="72"/>
      <path d="M62 2 l22 -2 l2 22 l-14 4 z"/><line x1="74" y1="26" x2="78" y2="64"/><line x1="68" y1="66" x2="88" y2="62"/>
      <path d="M42 40 q-4 4 0 8 q4 4 0 8 q-4 4 0 8"/><path d="M52 34 q-4 4 0 8 q4 4 0 8"/>
    </svg>
    <h3 style="top:6px;">Enjoy</h3>
    <p style="top:34px;">For wedding professions and couples to enjoy the wedding planning experience.</p>
  </div>

  <div class="value" style="top:774px;">
    <svg width="90" height="80" viewBox="0 0 90 80" aria-hidden="true" fill="none" stroke="var(--teal)" stroke-width="3" stroke-linecap="round">
      <line x1="36" y1="8" x2="36" y2="76"/>
      <path d="M36 2 q4 6 0 10 q-4 -4 0 -10z"/>
      <path d="M36 30 q-18 -10 -22 2 q10 10 22 4"/><path d="M36 24 q14 -10 20 0 q-8 8 -20 6"/>
      <path d="M36 52 q-18 -8 -22 4 q10 8 22 2"/><path d="M36 46 q16 -8 22 2 q-8 8 -22 6"/>
      <path d="M6 78 q30 -8 60 0"/>
    </svg>
    <h3 style="top:8px;">GROW</h3>
    <p style="top:32px;">Foster growth for our partners and within the wedding industry.</p>
  </div>

  <h1 class="section-title" style="top:914px;">ADVISORY BOARD</h1>
  <div class="divider" style="top:967px;" aria-hidden="true"></div>

  <article class="board" style="left:63px;">
    <div class="board-banner" role="img" aria-label="Teal to orange faceted pattern" style="background:linear-gradient(90deg,#2f8f86,#7aa060 45%,#f39a2a 75%,#ff8a12);"></div>
    <div class="board-avatar" role="img" aria-label="Portrait of Owen Hartley"></div>
    <div class="board-name">OWEN HARTLEY</div>
    <div class="board-role">Technical</div>
  </article>

  <article class="board" style="left:375px;">
    <div class="board-banner" role="img" aria-label="Yellow to orange faceted pattern" style="background:linear-gradient(90deg,#f7c21a,#f0a018 40%,#e06a1a 75%,#c0461a);"></div>
    <div class="board-avatar" role="img" aria-label="Portrait of Martin Cole"></div>
    <div class="board-name">MARTIN COLE</div>
    <div class="board-role">Marketing</div>
  </article>

  <article class="board" style="left:686px;">
    <div class="board-banner" role="img" aria-label="Slate to yellow faceted pattern" style="background:linear-gradient(90deg,#3a4e48,#8a8a30 35%,#d8b418 65%,#ffc814);"></div>
    <div class="board-avatar" role="img" aria-label="Portrait of Julian Pryce"></div>
    <div class="board-name">JULIAN PRYCE</div>
    <div class="board-role">Operations</div>
  </article>
</body>
</html>
```